First Annual Pemberton Family Reunion

Family reunion invitation, please see the attached letter for the language. Also provided a picture of my grandparents, if you could include it on a letter or brochure. I'm flexible.
Updates

I just uploaded a Word document with the time, address, and list of activities. Please click on the hyperlink, it takes you directly to our Family Reunion webpage and click on Agenda for all details.

Target Market(s)

Family and Friends invitation

Requirements
Must have
• Date, time, picture, family logo, and website for payment

```html
<!DOCTYPE html>
<html lang="en">
<head>
<meta charset="utf-8">
<title>Pemberton Family Reunion</title>
<link rel="stylesheet" href="https://fonts.googleapis.com/css2?family=Great+Vibes&family=Pinyon+Script&family=Lato:wght@300&display=swap">
<style>
  :root {
    --navy: #0f1f3d;
    --navy-deep: #0b1832;
    --gold: #cdb98c;
    --cream: #f5f1e6;
    --cream-light: #fbf9f3;
    --ink: #152448;
  }
  * { box-sizing: border-box; margin: 0; padding: 0; }
  html, body { width: 857px; height: 1200px; overflow: hidden; background: var(--navy); }
  .invitation {
    position: relative;
    width: 857px;
    height: 1200px;
    background: var(--navy);
    overflow: hidden;
  }
  .masthead {
    position: absolute;
    inset: 0 0 auto 0;
    height: 243px;
    background: linear-gradient(180deg, var(--navy-deep), var(--navy));
  }
  .family-name {
    position: absolute;
    top: 4px;
    left: 0;
    width: 100%;
    text-align: center;
    font-family: "Great Vibes", cursive;
    font-size: 108px;
    line-height: 1.2;
    color: var(--gold);
    text-shadow: 0 2px 3px rgba(0,0,0,.45);
  }
  .scroll {
    position: absolute;
    top: 92px;
    width: 170px;
    height: 26px;
    border-radius: 13px;
    background: linear-gradient(90deg, rgba(205,185,140,.15), rgba(205,185,140,.55), rgba(205,185,140,.15));
  }
  .scroll--left { left: 66px; }
  .scroll--right { right: 66px; }
  .event-title {
    position: absolute;
    top: 136px;
    left: 0;
    width: 100%;
    text-align: center;
    font-family: "Lato", sans-serif;
    font-weight: 300;
    font-size: 80px;
    letter-spacing: -1px;
    line-height: 1;
    color: var(--gold);
    text-shadow: 0 2px 3px rgba(0,0,0,.45);
  }
  .gallery {
    position: absolute;
    top: 243px;
    left: 0;
    width: 857px;
    height: 788px;
    background: var(--cream);
  }
  .grid {
    position: absolute;
    top: 2px;
    left: 26px;
    width: 805px;
    height: 786px;
    display: grid;
    grid-template-columns: 269px 268px 268px;
    grid-template-rows: 261px 263px 262px;
  }
  .cell {
    position: relative;
    display: flex;
    align-items: center;
    justify-content: center;
  }
  .quote {
    background: linear-gradient(135deg, var(--cream-light), var(--cream));
    font-family: "Pinyon Script", cursive;
    font-size: 29px;
    line-height: 48px;
    color: var(--ink);
    text-align: center;
    padding: 0 14px;
  }
  .quote--large { font-size: 33px; line-height: 52px; }
  .photo { box-shadow: inset 0 0 12px rgba(255,255,255,.6); }
  .photo--couple { background: linear-gradient(135deg, #d8cfc1, #6b4a3e 55%, #2a2528); }
  .photo--park { background: linear-gradient(160deg, #3f5a36, #7a2a3a 55%, #b9b2a8); }
  .photo--elders { background: #050505; }
  .photo--elders .portrait {
    width: 200px;
    height: 240px;
    background: linear-gradient(180deg, #6b5a4f, #e9e6e1 55%, #c9c3bd);
    opacity: .85;
  }
  .photo--group { background: linear-gradient(150deg, #d9d1b5, #3a2a2a 45%, #8e1f26 80%, #4a5a80); }
  .photo--selfie { background: linear-gradient(150deg, #3b3d44, #a9744e 45%, #d9a8a8 75%, #1d1d22); }
  .details {
    position: absolute;
    top: 1031px;
    left: 0;
    width: 100%;
    height: 169px;
    background: var(--navy);
    text-align: center;
    font-family: "Lato", sans-serif;
    font-weight: 300;
    color: var(--gold);
  }
  .details .date { margin-top: 9px; font-size: 34px; line-height: 40px; }
  .details .rsvp, .details .site { font-size: 40px; line-height: 48px; }
</style>
</head>
<body>
<main class="invitation">
  <header class="masthead">
    <div class="scroll scroll--left" role="img" aria-label="Gold scroll ornament"></div>
    <div class="scroll scroll--right" role="img" aria-label="Gold scroll ornament"></div>
    <h1>
      <span class="family-name">Pemberton</span>
      <span class="event-title">FAMILY REUNION</span>
    </h1>
  </header>

  <section class="gallery">
    <div class="grid">
      <div class="cell photo photo--couple" role="img" aria-label="Photo of a smiling couple"></div>
      <p class="cell quote">"The memories we<br>make with our<br>family is<br>everything."</p>
      <div class="cell photo photo--park" role="img" aria-label="Photo of two relatives in matching jackets outdoors"></div>

      <p class="cell quote quote--large">"Family is not<br>just an<br>important thing,<br>it's everything."</p>
      <div class="cell photo photo--elders">
        <div class="portrait" role="img" aria-label="Photo of the grandparents holding a baby"></div>
      </div>
      <p class="cell quote quote--large">"A family is a<br>little world<br>created by<br>love."</p>

      <div class="cell photo photo--group" role="img" aria-label="Group photo of family members at a gathering"></div>
      <p class="cell quote">"The love of a<br>family is life's<br>greatest blessing.",</p>
      <div class="cell photo photo--selfie" role="img" aria-label="Selfie of two relatives"></div>
    </div>
  </section>

  <footer class="details">
    <p class="date">SEP 21-23</p>
    <p class="rsvp">Please RSVP at:</p>
    <p class="site">Pembertonreunion.net</p>
  </footer>
</main>
</body>
</html>
```